Commercial and Multifamily informational website

We need a website for our commercial real estate management company. We will manage offices, retail, apartments and others. Here is the brief verbiage: Providing quality commercial and multifamily portfolio management to Landlords, REITs, and financial institutions. 

Industry/Entity Type

Real Estate

Number of Pages Required

2 page

Font styles to use
Sans Serif
Other font styles liked:
• Muli, Garamond

Colors
0555a3
5c5c5c
3176b5
85acd3
474747

Requirements
Must have
• Home page and contact page

```html
<!DOCTYPE html>
<html lang="en">
<head>
<meta charset="utf-8">
<title>Kelvane Property Group</title>
<link rel="stylesheet" href="https://fonts.googleapis.com/css2?family=Mulish:wght@400;600;700;800&display=swap">
<style>
:root{
  --blue:#0555a3;
  --blue-mid:#3176b5;
  --blue-light:#85acd3;
  --gray:#5c5c5c;
  --gray-dark:#474747;
  --box:#e6e6e6;
  --white:#ffffff;
  --text:#333333;
}
*{box-sizing:border-box;margin:0;padding:0}
html,body{width:1200px;height:4063px;overflow:hidden;background:var(--white)}
body{font-family:"Mulish",sans-serif;color:var(--text)}
.page{position:relative;width:1200px;height:4063px;overflow:hidden}
.abs{position:absolute}
a{color:inherit;text-decoration:none}

/* Hero */
.hero{position:absolute;left:0;top:0;width:1200px;height:710px;
  background:linear-gradient(180deg,#a7a4b4 0%,#c6b7b3 30%,#5a6474 55%,#6f7683 75%,#8a8f8e 100%)}
.header{position:absolute;left:0;top:0;width:1200px;height:135px;background:rgba(70,70,70,.72)}
.brand{position:absolute;left:87px;top:56px;display:flex;align-items:center;gap:14px;color:var(--white);font-weight:700;font-size:25px;letter-spacing:.5px}
.brand-square{width:34px;height:34px;border:3px solid var(--white)}
.topline{position:absolute;top:12px;left:700px;display:flex;align-items:center;font-size:12px;color:var(--white);gap:10px}
.topline .sep{width:1px;height:20px;background:rgba(255,255,255,.6);margin:0 14px}
.topline svg{width:16px;height:16px}
.nav{position:absolute;top:76px;left:640px;display:flex;font-size:14px;color:var(--white);font-weight:600}
.nav a{width:95px;text-align:center;position:relative;height:58px}
.nav a.active::after{content:"";position:absolute;left:20px;right:20px;bottom:0;height:5px;background:var(--white)}
.hero-title{position:absolute;left:260px;width:680px;top:345px;text-align:center;color:var(--white);font-weight:700;font-size:29px;line-height:34px}
.btn{position:absolute;height:54px;display:flex;align-items:center;justify-content:center;color:var(--white);font-weight:700;font-size:17px}
.btn-ghost{left:406px;width:168px;top:520px;background:rgba(60,60,60,.7)}
.btn-blue{left:618px;width:173px;top:520px;background:var(--blue-mid)}

/* Section headings */
.section-title{position:absolute;left:0;width:1200px;text-align:center;color:var(--blue);font-weight:700;font-size:36px}
.rule{position:absolute;left:560px;width:80px;height:3px;background:var(--blue-mid)}

.welcome-text{position:absolute;left:168px;width:864px;top:908px;text-align:center;font-size:16px;line-height:20px;color:#222;font-weight:600}

/* Feature boxes */
.feature{position:absolute;width:412px;height:111px;background:var(--box)}
.feature svg{position:absolute;left:38px;top:30px;width:52px;height:52px}
.feature h3{position:absolute;left:116px;top:20px;font-size:15px;color:var(--blue-mid);font-weight:600}
.feature p{position:absolute;left:116px;top:44px;width:270px;font-size:14px;line-height:18px;color:#444}

/* Property cards */
.prop-photo{position:absolute;width:262px;height:243px}
.prop-text{position:absolute;width:262px;font-size:17px;line-height:22px;color:#333}
.read-more{position:absolute;width:262px;font-size:17px;color:var(--blue-mid);display:flex;justify-content:space-between;align-items:center}
.read-more svg{width:22px;height:14px}
.view-more{position:absolute;left:501px;top:2292px;width:206px;height:48px;background:var(--gray);color:var(--white);font-size:19px;display:flex;align-items:center;justify-content:center;gap:22px}

/* Agents */
.agent-photo{position:absolute;width:262px;height:243px}
.agent-name{position:absolute;font-size:22px;color:#222;padding-left:20px;border-left:5px solid var(--gray-dark);line-height:26px;font-weight:600}
.agent-role{position:absolute;font-size:14px;color:#222}
.agent-line{position:absolute;font-size:14px;color:var(--blue-mid);display:flex;align-items:center;gap:18px}
.agent-line svg{width:24px;height:20px}

/* Info band */
.info-band{position:absolute;left:0;top:2972px;width:1200px;height:252px;background:var(--blue)}
.info-band h2{position:absolute;left:0;width:1200px;top:42px;text-align:center;color:var(--white);font-size:36px;font-weight:700}
.info-item{position:absolute;top:118px;display:flex;align-items:center;gap:18px;color:var(--white);font-size:22px;line-height:26px}
.info-item svg{width:42px;height:40px;flex:none}

/* Why choose */
.why-title{color:#111}
.rule-dark{background:#111}
.stat{position:absolute;width:260px;text-align:center}
.stat svg{width:64px;height:64px}
.stat .pct{font-size:28px;color:var(--gray-dark);margin-top:14px;font-weight:600}
.stat .label{font-size:20px;color:#333;margin-top:18px}

/* Footer */
.footer{position:absolute;left:0;top:3708px;width:1200px;height:355px;background:var(--gray)}
.footer-brand{position:absolute;left:135px;top:106px;display:flex;align-items:center;gap:12px;color:var(--white);font-weight:700;font-size:23px}
.social{position:absolute;top:222px;width:28px;height:28px;border-radius:50%;background:var(--white)}
.footer-head{position:absolute;top:54px;color:var(--white);font-size:26px;font-weight:700;padding-left:18px;border-left:5px solid var(--white);line-height:26px}
.footer-link{position:absolute;left:505px;color:var(--white);font-size:21px}
.footer-contact{position:absolute;left:772px;display:flex;align-items:flex-start;gap:16px;color:var(--white);font-size:21px;line-height:24px}
.footer-contact svg{width:26px;height:24px;flex:none;margin-top:2px}
.footer-rule{position:absolute;left:135px;top:293px;width:930px;height:1px;background:rgba(255,255,255,.5)}
.copyright{position:absolute;left:0;width:1200px;top:311px;text-align:center;color:var(--white);font-size:17px}
</style>
</head>
<body>
<div class="page">

  <!-- Hero -->
  <section class="hero" role="img" aria-label="Photograph of a two-storey suburban house with gabled roof and garage at dusk"></section>
  <header class="header">
    <div class="brand"><span class="brand-square"></span>Kelvane Property Group</div>
    <div class="topline">
      <svg viewBox="0 0 24 24" fill="#fff"><path d="M6.6 10.8a15 15 0 0 0 6.6 6.6l2.2-2.2a1 1 0 0 1 1-.25 11.4 11.4 0 0 0 3.6.57 1 1 0 0 1 1 1V20a1 1 0 0 1-1 1A17 17 0 0 1 3 4a1 1 0 0 1 1-1h3.5a1 1 0 0 1 1 1c0 1.25.2 2.45.57 3.6a1 1 0 0 1-.25 1z"/></svg>
      <span>(800) 123-4567</span>
      <span class="sep"></span>
      <svg viewBox="0 0 24 24" fill="none" stroke="#fff" stroke-width="2"><rect x="2" y="5" width="20" height="14"/><path d="M2 5l10 8 10-8"/></svg>
      <span>email@example.com</span>
      <span class="sep"></span>
      <span>Blog</span>
      <span class="sep"></span>
      <svg viewBox="0 0 24 24" fill="#fff"><circle cx="7" cy="12" r="2"/><circle cx="15" cy="12" r="2"/></svg>
    </div>
    <nav class="nav">
      <a class="active" href="#">HOME</a>
      <a href="#">ABOUT</a>
      <a href="#">AGENTS</a>
      <a href="#">SERVICES</a>
      <a href="#">CONTACT</a>
    </nav>
  </header>
  <h1 class="hero-title">Providing quality commercial and multifamily portfolio management to Landlords, REITs, and financial institutions.</h1>
  <a class="btn btn-ghost" href="#">KNOW MORE</a>
  <a class="btn btn-blue" href="#">CONTACT US</a>

  <!-- Welcome -->
  <h2 class="section-title" style="top:788px">WELCOME</h2>
  <div class="rule" style="top:849px"></div>
  <p class="welcome-text">Lorem ipsum dolor sit amet, consectetur adipiscing elit. Mauris luctus diam lectus, quis porttitor velit maximus in. Vestibulum imperdiet est et nibh mattis, nec congue ex posuere. Maecenas id metus luctus, auctor massa et, tincidunt risus. Duis luctus, ipsum ut accumsan tristique, sem lectus dapibus nunc, quis efficitur nunc orci sed diam. Morbi eu felis ipsum.</p>

  <div class="feature" style="left:168px;top:1048px">
    <svg viewBox="0 0 52 52" fill="none" stroke="#3176b5" stroke-width="2.5"><circle cx="26" cy="17" r="10"/><path d="M6 48c0-11 9-18 20-18s20 7 20 18z"/></svg>
    <h3>Agents</h3><p>Lorem ipsum dolor sit amet, consectetur adipiscing elit.</p>
  </div>
  <div class="feature" style="left:620px;top:1048px">
    <svg viewBox="0 0 52 52" fill="none" stroke="#3176b5" stroke-width="2.5"><path d="M26 48S11 31 11 20a15 15 0 0 1 30 0c0 11-15 28-15 28z"/><circle cx="26" cy="20" r="5"/></svg>
    <h3>Various Locations</h3><p>Lorem ipsum dolor sit amet, consectetur adipiscing elit.</p>
  </div>
  <div class="feature" style="left:168px;top:1200px">
    <svg viewBox="0 0 52 52" fill="none" stroke="#3176b5" stroke-width="2.5"><rect x="3" y="12" width="46" height="30"/><path d="M3 22h46M3 32h46M18 12v30M34 12v30"/></svg>
    <h3>View Appartments</h3><p>Lorem ipsum dolor sit amet, consectetur adipiscing elit.</p>
  </div>
  <div class="feature" style="left:620px;top:1200px">
    <svg viewBox="0 0 52 52" fill="none" stroke="#3176b5" stroke-width="2.5"><path d="M3 26s9-13 23-13 23 13 23 13-9 13-23 13S3 26 3 26z"/><circle cx="26" cy="26" r="6"/><path d="M8 44L44 8"/></svg>
    <h3>Privacy &amp; Security</h3><p>Lorem ipsum dolor sit amet, consectetur adipiscing elit.</p>
  </div>

  <!-- Properties -->
  <h2 class="section-title" style="top:1388px">Real Estate Propreties</h2>
  <div class="rule" style="top:1450px"></div>

  <div class="prop-photo" style="left:168px;top:1493px;background:linear-gradient(180deg,#3f82c9 0%,#8ab4de 40%,#9a5a46 60%,#4f7a3a 100%)" role="img" aria-label="Photo of a Tudor style brick house with lawn"></div>
  <div class="prop-photo" style="left:470px;top:1493px;background:linear-gradient(180deg,#dfe6ee 0%,#b9bfc6 40%,#3b3c40 70%,#6d6a66 100%)" role="img" aria-label="Photo of a modern glass and stone house"></div>
  <div class="prop-photo" style="left:770px;top:1493px;background:linear-gradient(180deg,#2c6fc2 0%,#7fb1e3 40%,#e9edf0 65%,#3f7a52 100%)" role="img" aria-label="Photo of a white modern villa with palm trees"></div>
  <p class="prop-text" style="left:168px;top:1764px">Lorem ipsum dolor sit amet, consectetur adipiscing elit.</p>
  <p class="prop-text" style="left:470px;top:1764px">Lorem ipsum dolor sit amet, consectetur adipiscing elit.</p>
  <p class="prop-text" style="left:770px;top:1764px">Lorem ipsum dolor sit amet, consectetur adipiscing elit.</p>
  <a class="read-more" style="left:168px;top:1817px" href="#">Read More<svg viewBox="0 0 22 14" fill="none" stroke="#3176b5" stroke-width="1.8"><path d="M0 7h20M14 1l6 6-6 6"/></svg></a>
  <a class="read-more" style="left:470px;top:1817px" href="#">Read More<svg viewBox="0 0 22 14" fill="none" stroke="#3176b5" stroke-width="1.8"><path d="M0 7h20M14 1l6 6-6 6"/></svg></a>
  <a class="read-more" style="left:770px;top:1817px" href="#">Read More<svg viewBox="0 0 22 14" fill="none" stroke="#3176b5" stroke-width="1.8"><path d="M0 7h20M14 1l6 6-6 6"/></svg></a>

  <div class="prop-photo" style="left:168px;top:1885px;background:linear-gradient(180deg,#5e95cf 0%,#dfe3e6 45%,#7b6a5a 70%,#3d6a33 100%)" role="img" aria-label="Photo of a Victorian mansion with wraparound porch"></div>
  <div class="prop-photo" style="left:470px;top:1885px;background:linear-gradient(180deg,#c9d8e6 0%,#6a6b6e 40%,#c8c2b4 65%,#5f8a3e 100%)" role="img" aria-label="Photo of a two-storey family house with front lawn"></div>
  <div class="prop-photo" style="left:770px;top:1885px;background:linear-gradient(180deg,#e8ecef 0%,#c9ced3 35%,#2e3237 65%,#4a4f55 100%)" role="img" aria-label="Photo of a dark modern house facade"></div>
  <p class="prop-text" style="left:168px;top:2157px">Lorem ipsum dolor sit amet, consectetur adipiscing elit.</p>
  <p class="prop-text" style="left:470px;top:2157px">Lorem ipsum dolor sit amet, consectetur adipiscing elit.</p>
  <p class="prop-text" style="left:770px;top:2157px">Lorem ipsum dolor sit amet, consectetur adipiscing elit.</p>
  <a class="read-more" style="left:168px;top:2210px" href="#">Read More<svg viewBox="0 0 22 14" fill="none" stroke="#3176b5" stroke-width="1.8"><path d="M0 7h20M14 1l6 6-6 6"/></svg></a>
  <a class="read-more" style="left:470px;top:2210px" href="#">Read More<svg viewBox="0 0 22 14" fill="none" stroke="#3176b5" stroke-width="1.8"><path d="M0 7h20M14 1l6 6-6 6"/></svg></a>
  <a class="read-more" style="left:770px;top:2210px" href="#">Read More<svg viewBox="0 0 22 14" fill="none" stroke="#3176b5" stroke-width="1.8"><path d="M0 7h20M14 1l6 6-6 6"/></svg></a>

  <a class="view-more" href="#">View More<svg width="10" height="16" viewBox="0 0 10 16" fill="none" stroke="#fff" stroke-width="2"><path d="M2 2l6 6-6 6"/></svg></a>

  <!-- Agents -->
  <h2 class="section-title" style="top:2420px">Agents You Can Trust</h2>
  <div class="rule" style="top:2480px"></div>

  <div class="agent-photo" style="left:168px;top:2525px;background:linear-gradient(160deg,#6f6f6a 0%,#a28d73 45%,#5b4a63 100%)" role="img" aria-label="Portrait photo of an agent"></div>
  <div class="agent-photo" style="left:470px;top:2525px;background:linear-gradient(160deg,#e4e2de 0%,#b39a86 45%,#4b4640 100%)" role="img" aria-label="Portrait photo of an agent"></div>
  <div class="agent-photo" style="left:770px;top:2525px;background:linear-gradient(160deg,#1a1a1a 0%,#5b3d2b 45%,#222 100%)" role="img" aria-label="Portrait photo of an agent"></div>

  <div class="agent-name" style="left:168px;top:2780px">JOHN DOE</div>
  <div class="agent-name" style="left:470px;top:2780px">JOHN DOE</div>
  <div class="agent-name" style="left:770px;top:2780px">JOHN DOE</div>
  <div class="agent-role" style="left:193px;top:2816px">Designer</div>
  <div class="agent-role" style="left:495px;top:2816px">Designer</div>
  <div class="agent-role" style="left:795px;top:2816px">Designer</div>

  <div class="agent-line" style="left:170px;top:2848px"><svg viewBox="0 0 24 20" fill="none" stroke="#3176b5" stroke-width="1.8"><rect x="1" y="2" width="22" height="16"/><path d="M1 2l11 9 11-9"/></svg>email@example.com</div>
  <div class="agent-line" style="left:472px;top:2848px"><svg viewBox="0 0 24 20" fill="none" stroke="#3176b5" stroke-width="1.8"><rect x="1" y="2" width="22" height="16"/><path d="M1 2l11 9 11-9"/></svg>email@example.com</div>
  <div class="agent-line" style="left:772px;top:2848px"><svg viewBox="0 0 24 20" fill="none" stroke="#3176b5" stroke-width="1.8"><rect x="1" y="2" width="22" height="16"/><path d="M1 2l11 9 11-9"/></svg>email@example.com</div>
  <div class="agent-line" style="left:170px;top:2886px"><svg viewBox="0 0 24 24" fill="#3176b5"><path d="M6.6 10.8a15 15 0 0 0 6.6 6.6l2.2-2.2a1 1 0 0 1 1-.25 11.4 11.4 0 0 0 3.6.57 1 1 0 0 1 1 1V20a1 1 0 0 1-1 1A17 17 0 0 1 3 4a1 1 0 0 1 1-1h3.5a1 1 0 0 1 1 1c0 1.25.2 2.45.57 3.6a1 1 0 0 1-.25 1z"/></svg>(123) 456 789</div>
  <div class="agent-line" style="left:472px;top:2886px"><svg viewBox="0 0 24 24" fill="#3176b5"><path d="M6.6 10.8a15 15 0 0 0 6.6 6.6l2.2-2.2a1 1 0 0 1 1-.25 11.4 11.4 0 0 0 3.6.57 1 1 0 0 1 1 1V20a1 1 0 0 1-1 1A17 17 0 0 1 3 4a1 1 0 0 1 1-1h3.5a1 1 0 0 1 1 1c0 1.25.2 2.45.57 3.6a1 1 0 0 1-.25 1z"/></svg>(123) 456 789</div>
  <div class="agent-line" style="left:772px;top:2886px"><svg viewBox="0 0 24 24" fill="#3176b5"><path d="M6.6 10.8a15 15 0 0 0 6.6 6.6l2.2-2.2a1 1 0 0 1 1-.25 11.4 11.4 0 0 0 3.6.57 1 1 0 0 1 1 1V20a1 1 0 0 1-1 1A17 17 0 0 1 3 4a1 1 0 0 1 1-1h3.5a1 1 0 0 1 1 1c0 1.25.2 2.45.57 3.6a1 1 0 0 1-.25 1z"/></svg>(123) 456 789</div>

  <!-- Info band -->
  <section class="info-band">
    <h2>Need More Information ?</h2>
    <div class="info-item" style="left:168px"><svg viewBox="0 0 24 24" fill="#fff"><path d="M6.6 10.8a15 15 0 0 0 6.6 6.6l2.2-2.2a1 1 0 0 1 1-.25 11.4 11.4 0 0 0 3.6.57 1 1 0 0 1 1 1V20a1 1 0 0 1-1 1A17 17 0 0 1 3 4a1 1 0 0 1 1-1h3.5a1 1 0 0 1 1 1c0 1.25.2 2.45.57 3.6a1 1 0 0 1-.25 1z"/></svg>(123) 456-789</div>
    <div class="info-item" style="left:471px"><svg viewBox="0 0 42 40" fill="none" stroke="#fff" stroke-width="2.2"><rect x="2" y="6" width="38" height="28"/><path d="M2 6l19 16L40 6"/></svg>email@example.com</div>
    <div class="info-item" style="left:772px"><svg viewBox="0 0 42 40" fill="none" stroke="#fff" stroke-width="2.2"><path d="M21 34S10 22 10 14a11 11 0 0 1 22 0c0 8-11 20-11 20z"/><circle cx="21" cy="14" r="4"/><path d="M6 38h30"/></svg><span>1234 Street Name,<br>City Name</span></div>
  </section>

  <!-- Why choose -->
  <h2 class="section-title why-title" style="top:3300px">Why Choose US ?</h2>
  <div class="rule rule-dark" style="top:3372px"></div>

  <div class="stat" style="left:92px;top:3420px">
    <svg viewBox="0 0 64 64" fill="none" stroke="#474747" stroke-width="2.5"><circle cx="32" cy="20" r="12"/><path d="M8 60c0-14 10-22 24-22s24 8 24 22z"/></svg>
    <div class="pct">80%</div><div class="label">Satisfied Customers</div>
  </div>
  <div class="stat" style="left:339px;top:3420px">
    <svg viewBox="0 0 64 64" fill="#474747"><path d="M2 52l20-32 12 18 8-10 20 24z"/></svg>
    <div class="pct">70%</div><div class="label">Partners</div>
  </div>
  <div class="stat" style="left:607px;top:3420px">
    <svg viewBox="0 0 64 64" fill="none" stroke="#474747" stroke-width="2.5"><rect x="6" y="10" width="52" height="36"/><path d="M14 20h36M14 28h36M14 36h24M32 46v10M22 58h20"/></svg>
    <div class="pct">95%</div><div class="label">Project Done</div>
  </div>
  <div class="stat" style="left:845px;top:3420px">
    <svg viewBox="0 0 64 64" fill="#474747"><path d="M32 6A26 26 0 1 0 58 32H32z"/><path d="M36 2v26h26A26 26 0 0 0 36 2z"/></svg>
    <div class="pct">65%</div><div class="label">Business Plans</div>
  </div>

  <!-- Footer -->
  <footer class="footer">
    <div class="footer-brand"><span class="brand-square"></span>Kelvane Property Group</div>
    <span class="social" style="left:176px" aria-label="Social link"></span>
    <span class="social" style="left:219px" aria-label="Social link"></span>
    <span class="social" style="left:265px" aria-label="Social link"></span>

    <div class="footer-head" style="left:471px">Pages</div>
    <a class="footer-link" style="top:105px" href="#">Home</a>
    <a class="footer-link" style="top:143px" href="#">About</a>
    <a class="footer-link" style="top:181px" href="#">Sevices</a>
    <a class="footer-link" style="top:216px" href="#">Agents</a>

    <div class="footer-head" style="left:772px">Contact</div>
    <div class="footer-contact" style="top:107px"><svg viewBox="0 0 26 24" fill="none" stroke="#fff" stroke-width="1.8"><path d="M13 20S6 13 6 8a7 7 0 0 1 14 0c0 5-7 12-7 12z"/><circle cx="13" cy="8" r="2.5"/><path d="M4 23h18"/></svg><span>1234 Street Name,<br>City Name</span></div>
    <div class="footer-contact" style="top:178px"><svg viewBox="0 0 24 24" fill="#fff"><path d="M6.6 10.8a15 15 0 0 0 6.6 6.6l2.2-2.2a1 1 0 0 1 1-.25 11.4 11.4 0 0 0 3.6.57 1 1 0 0 1 1 1V20a1 1 0 0 1-1 1A17 17 0 0 1 3 4a1 1 0 0 1 1-1h3.5a1 1 0 0 1 1 1c0 1.25.2 2.45.57 3.6a1 1 0 0 1-.25 1z"/></svg>(123) 456 789</div>
    <div class="footer-contact" style="top:224px"><svg viewBox="0 0 26 24" fill="none" stroke="#fff" stroke-width="1.8"><rect x="2" y="4" width="22" height="16"/><path d="M2 4l11 9 11-9"/></svg>email@example.com</div>

    <div class="footer-rule"></div>
    <p class="copyright">Copyright 2017 - All Rights Reserved</p>
  </footer>

</div>
</body>
</html>
```